Mentorloft needs a WordPress - Design

I am a personal, team and business coach and help my clients to develop their potential. I mainly work with individuals and teams, but this can also be in the context of a company.
My business is called "Mentorloft"

The main goal of this website is to promote my business and to attire new customers.
I also want to present my concepts and ideas about coaching and how I actually do coaching and consulting. This is also to inform potential customers what coaching actually is and what it's not.
I want to host this website on a hosting-provider and want to be able to add and adapt content on my own. I'm thus looking for a WordPress - design.

Content:

vision
• Why do I do this
• How do I do this
• What am I doing

Coaching
• Career development
• Conflicts
• What is coaching, why coaching
• Conduct of a session and of the whole consultation
Limits of coaching
• Examples of positive effects of coaching

Support concept

Blog about current topics

Left

About me

Contact form

Footer / disclaimer

The following topics are the most important parts of my daily work as a coach with my clients, maybe this helps to get choos a suitable design:
- personality development, analyzing aspects and patterns and showing their influence
- Improve collaboration and cooperation in teams
- Addressing and solving conflicts (private and business)
- Identify and foster motivation, drivers, goals and action patterns
- Define next steps for the further improvement
- Accompany reorientation in professional career
- Discovering and using the strengths of the customers

The major part of my work is direct conversation with the customer, on site or virtually. My job is to support the customer in recognizing his own ideas, goals and possibilities and to define next steps in the desired direction

Target Market(s)

Small businesses and private persons in serch of a professional coach

Industry/Entity Type

Consultant

Number of Pages Required

1 page

Font styles to use
Sans Serif

Requirements
Must have
• - Logo / Name (see attachment)
- Menu, fixed navigation
- content
- blog
- Footer (contact, disclaimer)

- I need a WordPress design suitable for Mobile and Desktop devices.
- I'm looking for a modern, friendly and easy to use web site.
- First page as Long-pager (scrolling), other pages as long-pager or standard
- Decent, friendly colors but still clear, simple
Nice to have
• - Panorama image (image changing on every load of the site)
- Quote (changing on every load of the site)

```html
<!DOCTYPE html>
<html lang="en">
<head>
<meta charset="utf-8">
<title>Mentorloft – Personal, Team and Business Coaching</title>
<link rel="stylesheet" href="https://fonts.googleapis.com/css2?family=Montserrat:wght@700;800&family=Oswald:wght@500&family=Roboto:wght@400;500;700&display=swap">
<style>
:root{
  --cyan:#1db4ea;
  --navy:#2d2f8f;
  --ink:#1a1a1a;
  --text:#3a3a3a;
  --muted:#8a8a8a;
  --dark:#111216;
  --light:#efefef;
  --line:#d8d8d8;
  --white:#ffffff;
}
*{box-sizing:border-box;margin:0;padding:0}
html,body{width:1200px;height:4987px;overflow:hidden}
body{font-family:"Roboto",Arial,sans-serif;color:var(--text);background:var(--white)}
section,header,footer{position:relative;width:1200px;overflow:hidden}
.abs{position:absolute}
.btn{position:absolute;background:var(--cyan);color:var(--white);font:700 13px "Roboto",sans-serif;display:flex;align-items:center;justify-content:center;border-radius:4px;text-transform:uppercase;letter-spacing:.3px}
.mark{position:absolute;width:44px;height:44px;background:var(--navy);border:6px solid var(--cyan)}
.section-title{position:absolute;left:0;width:1200px;text-align:center;font:500 40px "Oswald",sans-serif;color:var(--ink);text-transform:uppercase;display:flex;justify-content:center;align-items:center;gap:22px;line-height:1}
.section-title::before,.section-title::after{content:"";width:70px;height:3px;background:var(--navy)}
.section-sub{position:absolute;left:0;width:1200px;text-align:center;font-size:15px;color:var(--muted)}
.photo{position:absolute}

/* hero */
.hero{height:718px;background:var(--dark)}
.hero-photo{inset:0;background:radial-gradient(ellipse at 70% 40%,#4a4036 0%,#2a2620 40%,#121214 80%)}
.topbar{position:absolute;right:99px;top:20px;display:flex;gap:30px;color:#cfcfcf;font-size:13px}
.topbar span{display:flex;align-items:center;gap:8px}
.brand{position:absolute;display:flex;align-items:center;gap:10px;font:500 20px "Roboto",sans-serif;color:var(--cyan);letter-spacing:1px}
.brand i{width:14px;height:14px;background:var(--cyan);display:block}
.nav{position:absolute;right:99px;top:72px;display:flex;gap:30px;font-size:14px;color:var(--white);text-transform:uppercase}
.nav .active{color:var(--cyan);position:relative}
.nav .active::after{content:"";position:absolute;left:-12px;right:-12px;top:45px;height:3px;background:var(--cyan)}
.nav-rule{position:absolute;left:99px;width:1002px;top:126px;height:1px;background:rgba(255,255,255,.35)}
.hero h1{position:absolute;left:99px;top:278px;font:800 50px/52px "Montserrat",sans-serif;color:var(--white);text-transform:uppercase}
.hero p{position:absolute;left:99px;top:402px;width:500px;color:var(--white);font-size:16px;line-height:21px}

/* about */
.about{height:710px}
.about h2{position:absolute;left:99px;top:180px;font:500 40px "Oswald",sans-serif;color:var(--ink);display:flex;align-items:center;gap:22px;text-transform:uppercase}
.about h2::after{content:"";width:68px;height:3px;background:var(--navy)}
.about h3{position:absolute;left:99px;top:260px;font:500 29px/34px "Roboto",sans-serif;color:var(--ink)}
.about p{position:absolute;left:99px;top:344px;width:458px;font-size:13.5px;line-height:19.5px;color:var(--text)}
.about-photo{left:608px;top:87px;width:493px;height:476px;border:5px solid #b9b9b9;background:linear-gradient(135deg,#cfd5d8 0%,#9aa8b3 45%,#4b6e9b 75%,#2e4b73 100%)}

/* vision */
.vision{height:730px;background:var(--dark)}
.vision-photo{inset:0;background:radial-gradient(ellipse at 50% 60%,#2a2a2e 0%,#17171a 60%,#0e0e10 100%)}
.vision .section-title,.vision .section-sub{color:var(--white)}
.vision .section-title::before,.vision .section-title::after{background:var(--white)}
.vision .section-sub{color:#bdbdbd}
.pillar{position:absolute;top:284px;width:310px;height:356px;text-align:center;color:var(--white)}
.pillar svg.shape{position:absolute;left:0;top:48px}
.pillar .icon{position:absolute;left:106px;top:0;width:98px;height:98px;border-radius:50%;background:var(--white);display:flex;align-items:center;justify-content:center}
.pillar h4{position:absolute;left:0;width:310px;top:167px;font:700 20px "Roboto",sans-serif}
.pillar p{position:absolute;left:55px;width:200px;top:200px;font-size:13.5px;line-height:18px}
.pillar a{position:absolute;left:0;width:310px;top:277px;font-size:13px;color:var(--white);text-decoration:none;text-transform:uppercase}
.pillar.on a{text-decoration:underline}

/* coaching */
.coaching{height:909px}
.card{position:absolute;background:var(--white);border:1px solid var(--line);text-align:center}
.coach-card{top:272px;width:322px;height:502px}
.coach-card .photo{left:0;top:0;width:100%;height:312px}
.coach-card h4{position:absolute;left:0;width:100%;top:344px;font:500 20px/23px "Roboto",sans-serif;color:var(--ink)}
.coach-card p{position:absolute;left:24px;right:24px;top:400px;font-size:13.5px;line-height:21px}
.coach-card a{position:absolute;left:0;width:100%;top:466px;font:500 13px "Roboto",sans-serif;color:var(--ink);text-decoration:none;text-transform:uppercase}
.coach-card.on{box-shadow:0 6px 14px rgba(29,180,234,.25)}
.coach-card.on h4,.coach-card.on a{color:var(--navy)}
.coach-card.on a{text-decoration:underline}
.pager{position:absolute;left:0;width:1200px;top:808px;display:flex;justify-content:center;gap:10px}
.pager i{width:9px;height:9px;border-radius:50%;border:1px solid var(--navy);display:block}
.pager i.on{background:var(--navy)}

/* topics */
.topics{height:886px;background:var(--light)}
.post{top:269px;width:320px;height:530px;border-radius:6px;overflow:visible}
.post .photo{left:0;top:0;width:100%;height:288px;border-radius:6px 6px 0 0}
.post .meta{position:absolute;left:18px;right:18px;top:259px;height:54px;background:var(--white);border-radius:4px;box-shadow:0 2px 6px rgba(0,0,0,.12);display:flex;align-items:center;justify-content:center;gap:28px;font-size:12px;color:var(--muted)}
.post .meta span{display:flex;align-items:center;gap:6px}
.post .meta b{font-weight:400;color:var(--navy)}
.post h4{position:absolute;left:20px;right:20px;top:352px;font:700 21px/26px "Roboto",sans-serif;color:var(--ink);text-transform:uppercase}
.post p{position:absolute;left:24px;right:24px;top:418px;font-size:13.5px;line-height:20px}
.post .go{position:absolute;left:141px;top:469px;width:38px;height:38px;border-radius:50%;background:#9a9a9a;display:flex;align-items:center;justify-content:center}
.post.on{border:2px solid var(--cyan)}
.post.on h4{color:var(--navy)}
.post.on .go{background:var(--cyan)}

/* contact */
.contact{height:625px;background:#fafafa}
.field{position:absolute;background:#f0f0f0;border:1px solid #a9a9a9;border-radius:5px;font-size:14px;color:var(--ink);padding:0 20px;display:flex;align-items:center}
.field.msg{align-items:flex-start;padding-top:18px}

/* footer */
.footer{height:409px;background:var(--dark)}
.footer-photo{inset:0;background:radial-gradient(ellipse at 50% 40%,#2b2b30 0%,#151518 60%,#0c0c0e 100%)}
.footer .brand{left:0;width:1200px;justify-content:center;top:82px;font-size:22px}
.quick{position:absolute;left:0;width:1200px;text-align:center;top:186px;font:700 15px "Roboto",sans-serif;color:var(--white);text-transform:uppercase}
.reach{position:absolute;left:0;width:1200px;top:242px;display:flex;justify-content:center;gap:50px;color:var(--white);font-size:15px}
.reach span{display:flex;align-items:center;gap:10px}
.foot-rule{position:absolute;left:99px;width:1002px;top:297px;height:1px;background:rgba(255,255,255,.3)}
.foot-nav{position:absolute;left:0;width:1200px;top:322px;display:flex;justify-content:center;gap:30px;color:var(--white);font-size:14px;text-transform:uppercase}
.foot-nav .active{color:var(--cyan)}
.copy{position:absolute;left:0;width:1200px;top:378px;text-align:center;font-size:12px;color:#8c8c8c}
.copy b{font-weight:400;color:var(--cyan)}
</style>
</head>
<body>

<header class="hero">
  <div class="photo hero-photo" role="img" aria-label="Dim photo of a coach and clients working together around a table"></div>
  <div class="topbar">
    <span><svg width="16" height="11" viewBox="0 0 16 11"><rect x=".5" y=".5" width="15" height="10" fill="none" stroke="#cfcfcf"/><path d="M.5 .5 8 6l7.5-5.5" fill="none" stroke="#cfcfcf"/></svg>hello@mentorloft.com</span>
    <span><svg width="14" height="14" viewBox="0 0 24 24"><path fill="#cfcfcf" d="M6.6 10.8a15 15 0 0 0 6.6 6.6l2.2-2.2c.3-.3.7-.4 1-.2 1.1.4 2.3.6 3.6.6.6 0 1 .4 1 1V20c0 .6-.4 1-1 1A17 17 0 0 1 3 4c0-.6.4-1 1-1h3.5c.6 0 1 .4 1 1 0 1.3.2 2.5.6 3.6.1.3 0 .7-.2 1z"/></svg>(555) 0142 3386 20</span>
  </div>
  <div class="brand" style="left:95px;top:46px"><i></i>Mentorloft</div>
  <nav class="nav"><span class="active">Home</span><span>About</span><span>Vision</span><span>Coaching</span><span>Blog</span><span>Contact</span></nav>
  <div class="nav-rule"></div>
  <h1>Lorem ipsum dolor<br>sit amet adipiscing</h1>
  <p>Lorem ipsum dolor sit amet, consectetur adipiscing elit. Duis ornare maximus porta.</p>
  <div class="btn" style="left:99px;top:464px;width:134px;height:45px">Read more</div>
</header>

<section class="about">
  <div class="mark" style="left:99px;top:114px"></div>
  <h2>About us</h2>
  <h3>Lorem Ipsum Dolor Sit Amet,<br>Consectetur Adipiscing Elit.</h3>
  <p>Lorem ipsum dolor sit amet, consectetur adipiscing elit. Duis ornare maximus porta. Integer euismod nibh ac vehicula maximus. Nam molestie venenatis turpis, eu elementum mauris tristique sit amet. Proin massa enim, imperdiet eu turpis eget, finibus suscipit elit. Vestibulum dignissim vestibulum orci, nec dapibus risus efficitur ac. In ac rutrum lacus, quis ullamcorper ligula. Maecenas semper, lacus id iaculis fringilla, dui nisl egestas nulla, sit amet faucibus mi felis sed purus.</p>
  <div class="btn" style="left:99px;top:507px;width:134px;height:45px">Read more</div>
  <div class="photo about-photo" role="img" aria-label="Photo of a smiling coach in a blue shirt at a meeting table"></div>
</section>

<section class="vision">
  <div class="photo vision-photo" role="img" aria-label="Dark photo of a team meeting"></div>
  <div class="mark" style="left:578px;top:91px"></div>
  <h2 class="section-title" style="top:162px">Vision</h2>
  <p class="section-sub" style="top:222px">Lorem ipsum dolor sit amet, consectetur adipiscing elit. Duis ornare maximus porta.</p>

  <div class="pillar on" style="left:110px">
    <svg class="shape" width="310" height="308"><polygon points="155,0 310,154 155,308 0,154" fill="#1db4ea"/></svg>
    <div class="icon"><svg width="50" height="44" viewBox="0 0 50 44" fill="none" stroke="#222" stroke-width="2"><rect x="3" y="6" width="38" height="30"/><path d="M3 12h38M10 30v-8M16 30v-12M22 30v-6M28 30v-10"/><circle cx="40" cy="34" r="7"/></svg></div>
    <h4>Why Do I Do This</h4>
    <p>Lorem ipsum dolor sit amet, consectetur adipiscing elit. Duis ornare maximus porta.</p>
    <a>Read more</a>
  </div>
  <div class="pillar" style="left:449px">
    <svg class="shape" width="310" height="308"><polygon points="155,1 309,154 155,307 1,154" fill="none" stroke="#cfcfcf"/></svg>
    <div class="icon"><svg width="46" height="46" viewBox="0 0 46 46" fill="none" stroke="#222" stroke-width="2"><circle cx="23" cy="8" r="5"/><path d="M23 13v8M8 21h30M8 21v6M23 21v6M38 21v6"/><circle cx="8" cy="32" r="4"/><circle cx="23" cy="32" r="4"/><circle cx="38" cy="32" r="4"/><path d="M2 44h42"/></svg></div>
    <h4>How Do I Do This</h4>
    <p>Lorem ipsum dolor sit amet, consectetur adipiscing elit. Duis ornare maximus porta.</p>
    <a>Read more</a>
  </div>
  <div class="pillar" style="left:784px">
    <svg class="shape" width="310" height="308"><polygon points="155,1 309,154 155,307 1,154" fill="none" stroke="#cfcfcf"/></svg>
    <div class="icon"><svg width="50" height="46" viewBox="0 0 50 46" fill="none" stroke="#222" stroke-width="2"><circle cx="25" cy="10" r="8"/><path d="M25 5v10M22 7h5M22 13h5"/><path d="M2 26l10-4 8 6 6-2 8 6-10 8-10-6-12-2zM48 26l-10-4-10 6"/></svg></div>
    <h4>What Am I Doing</h4>
    <p>Lorem ipsum dolor sit amet, consectetur adipiscing elit. Duis ornare maximus porta.</p>
    <a>Read more</a>
  </div>
</section>

<section class="coaching">
  <div class="mark" style="left:578px;top:90px"></div>
  <h2 class="section-title" style="top:164px">Coaching</h2>
  <p class="section-sub" style="top:216px">Lorem ipsum dolor sit amet, consectetur adipiscing elit. Duis ornare maximus porta.</p>

  <article class="card coach-card on" style="left:99px">
    <div class="photo" role="img" aria-label="Photo of a career workshop with a presenter and attendees" style="background:linear-gradient(160deg,#d9d3cc,#a39a90 55%,#5e5a58)"></div>
    <h4>Career Development</h4>
    <p>Lorem ipsum dolor sit amet, consectetur adipiscing elit. Duis maximus porta.</p>
    <a>Read more</a>
  </article>
  <article class="card coach-card" style="left:439px">
    <div class="photo" role="img" aria-label="Photo of three colleagues in a tense discussion" style="background:linear-gradient(160deg,#c9b7a8,#8b7263 55%,#3f3a3a)"></div>
    <h4>Conflicts</h4>
    <p>Lorem ipsum dolor sit amet, consectetur adipiscing elit. Duis maximus porta.</p>
    <a>Read more</a>
  </article>
  <article class="card coach-card" style="left:779px">
    <div class="photo" role="img" aria-label="Photo of a bright boardroom with a team seated around a long table" style="background:linear-gradient(180deg,#e6e9ea,#b5babd 55%,#4a4d52)"></div>
    <h4>What Is Coaching,<br>Why Coaching</h4>
    <p style="top:408px">Lorem ipsum dolor sit amet, consectetur adipiscing elit. Duis maximus porta.</p>
    <a style="top:472px">Read more</a>
  </article>
  <div class="pager"><i class="on"></i><i></i><i></i></div>
</section>

<section class="topics">
  <div class="mark" style="left:578px;top:91px"></div>
  <h2 class="section-title" style="top:163px">Current Topics</h2>
  <p class="section-sub" style="top:216px">Lorem ipsum dolor sit amet, consectetur adipiscing elit. Duis ornare maximus porta.</p>

  <article class="card post on" style="left:99px">
    <div class="photo" role="img" aria-label="Photo of colleagues laughing together at an office meeting" style="background:linear-gradient(160deg,#e3e3e3,#a9a6a3 55%,#4b4a4e)"></div>
    <div class="meta"><span><svg width="14" height="14" viewBox="0 0 14 14" fill="none" stroke="#888"><rect x="1" y="2" width="12" height="11"/><path d="M1 5h12M4 0v3M10 0v3"/></svg><b style="color:#333">26 July</b></span><span><svg width="12" height="13" viewBox="0 0 12 13" fill="none" stroke="#888"><circle cx="6" cy="4" r="3"/><path d="M1 13c0-3 2-5 5-5s5 2 5 5"/></svg><b>Posted by</b> <span style="color:#333">Your Name</span></span></div>
    <h4>Lorem ipsum dolor sit amet, consectetur</h4>
    <p>Lorem ipsum dolor sit amet, consectetur adipiscing elit. Duis ornare porta.</p>
    <div class="go"><svg width="12" height="12" viewBox="0 0 12 12"><path d="M4 2l4 4-4 4" fill="none" stroke="#fff" stroke-width="2"/></svg></div>
  </article>
  <article class="card post" style="left:439px">
    <div class="photo" role="img" aria-label="Photo of team members stacking their hands together" style="background:linear-gradient(160deg,#d8c0a4,#a68566 55%,#6b5040)"></div>
    <div class="meta"><span><svg width="14" height="14" viewBox="0 0 14 14" fill="none" stroke="#888"><rect x="1" y="2" width="12" height="11"/><path d="M1 5h12M4 0v3M10 0v3"/></svg>26 July</span><span><svg width="12" height="13" viewBox="0 0 12 13" fill="none" stroke="#888"><circle cx="6" cy="4" r="3"/><path d="M1 13c0-3 2-5 5-5s5 2 5 5"/></svg><b>Posted by</b> Your Name</span></div>
    <h4>Lorem ipsum dolor sit amet, consectetur</h4>
    <p>Lorem ipsum dolor sit amet, consectetur adipiscing elit. Duis ornare porta.</p>
    <div class="go"><svg width="12" height="12" viewBox="0 0 12 12"><path d="M4 2l4 4-4 4" fill="none" stroke="#fff" stroke-width="2"/></svg></div>
  </article>
  <article class="card post" style="left:780px">
    <div class="photo" role="img" aria-label="Photo of a coach talking with a client in a bright office" style="background:linear-gradient(160deg,#eef0ef,#b8bcbd 50%,#3d4650)"></div>
    <div class="meta"><span><svg width="14" height="14" viewBox="0 0 14 14" fill="none" stroke="#888"><rect x="1" y="2" width="12" height="11"/><path d="M1 5h12M4 0v3M10 0v3"/></svg>26 July</span><span><svg width="12" height="13" viewBox="0 0 12 13" fill="none" stroke="#888"><circle cx="6" cy="4" r="3"/><path d="M1 13c0-3 2-5 5-5s5 2 5 5"/></svg><b>Posted by</b> Your Name</span></div>
    <h4>Lorem ipsum dolor sit amet, consectetur</h4>
    <p>Lorem ipsum dolor sit amet, consectetur adipiscing elit. Duis ornare porta.</p>
    <div class="go"><svg width="12" height="12" viewBox="0 0 12 12"><path d="M4 2l4 4-4 4" fill="none" stroke="#fff" stroke-width="2"/></svg></div>
  </article>
</section>

<section class="contact">
  <div class="mark" style="left:578px;top:91px"></div>
  <h2 class="section-title" style="top:161px">Contact us</h2>
  <p class="section-sub" style="top:219px">Lorem ipsum dolor sit amet, consectetur adipiscing elit. Duis ornare maximus porta.</p>
  <div class="field" style="left:118px;top:281px;width:307px;height:44px">Name</div>
  <div class="field" style="left:447px;top:281px;width:307px;height:44px">Email</div>
  <div class="field" style="left:774px;top:281px;width:307px;height:44px">Phone</div>
  <div class="field msg" style="left:118px;top:343px;width:963px;height:104px">Message</div>
  <div class="btn" style="left:532px;top:494px;width:136px;height:42px">Submit</div>
</section>

<footer class="footer">
  <div class="photo footer-photo" role="img" aria-label="Dark photo of a group discussion"></div>
  <div class="brand"><i></i>Mentorloft</div>
  <div class="quick">Quick links</div>
  <div class="reach">
    <span><svg width="16" height="22" viewBox="0 0 16 22"><path d="M8 1a7 7 0 0 0-7 7c0 5 7 13 7 13s7-8 7-13a7 7 0 0 0-7-7z" fill="none" stroke="#1db4ea" stroke-width="2"/><circle cx="8" cy="8" r="2.5" fill="#1db4ea"/></svg>Your address will be here</span>
    <span><svg width="20" height="20" viewBox="0 0 24 24"><path fill="#1db4ea" d="M6.6 10.8a15 15 0 0 0 6.6 6.6l2.2-2.2c.3-.3.7-.4 1-.2 1.1.4 2.3.6 3.6.6.6 0 1 .4 1 1V20c0 .6-.4 1-1 1A17 17 0 0 1 3 4c0-.6.4-1 1-1h3.5c.6 0 1 .4 1 1 0 1.3.2 2.5.6 3.6.1.3 0 .7-.2 1z"/></svg>(555) 0142 3386 20</span>
    <span><svg width="26" height="18" viewBox="0 0 26 18"><rect x="1" y="1" width="24" height="16" fill="none" stroke="#1db4ea" stroke-width="2"/><path d="M1 1l12 9 12-9" fill="none" stroke="#1db4ea" stroke-width="2"/></svg>hello@mentorloft.com</span>
  </div>
  <div class="foot-rule"></div>
  <nav class="foot-nav"><span class="active">Home</span><span>About</span><span>Vision</span><span>Coaching</span><span>Blog</span><span>Contact</span></nav>
  <p class="copy">Copyright © 2020 <b>Mentorloft</b>. All Rights Reserved.</p>
</footer>

</body>
</html>
```